TwistyLanesCamp.com

Current website needs redesign to make it more attractive and easier to Navigate. Currently being hosted on net porter. Can be accessed at
www,twistylanescamp.com.

```html
<!DOCTYPE html>
<html lang="en">
<head>
<meta charset="utf-8">
<title>TwistyLanes Camp</title>
<link href="https://fonts.googleapis.com/css2?family=Exo+2:wght@600;700;800&family=Roboto:wght@400;500;700&display=swap" rel="stylesheet">
<style>
:root{
  --red:#d0202c;
  --red-soft:#e35a62;
  --black:#0c0c0c;
  --white:#ffffff;
  --text:#222222;
  --muted:#555555;
  --field:#c8202a;
}
*{box-sizing:border-box;margin:0;padding:0}
html,body{width:1200px;height:5025px;overflow:hidden;background:var(--white)}
body{font-family:"Roboto",sans-serif;color:var(--text);position:relative}
.page{position:relative;width:1200px;height:5025px;overflow:hidden}
.abs{position:absolute}
.heading{font-family:"Exo 2",sans-serif;font-weight:800;letter-spacing:1px}
.heading .accent{color:var(--red)}

/* header */
.topbar{left:0;top:0;width:1200px;height:152px}
.brand{left:40px;top:26px;display:flex;align-items:center;gap:12px}
.brand-dot{width:46px;height:46px;background:var(--red);border-radius:50%}
.brand-name{font-family:"Exo 2",sans-serif;font-weight:800;font-size:34px;color:var(--black);line-height:1}
.brand-name small{display:block;font-size:14px;letter-spacing:4px;text-align:right}
.contact-strip{left:503px;top:0;width:697px;height:68px}
.contact-strip .item{position:absolute;top:20px;color:var(--white);font-size:15px;display:flex;align-items:center;gap:10px}
.phone-box{border:2px solid var(--white);padding:4px 22px;font-weight:700;font-size:17px}
.nav{top:98px;left:348px;display:flex;gap:28px;font-family:"Exo 2",sans-serif;font-weight:700;font-size:18px;color:var(--red)}

/* hero */
.hero{left:0;top:152px;width:1200px;height:576px;background:linear-gradient(100deg,#6e5418 0%,#b0892c 35%,#d8c88e 60%,#8a7a4c 100%)}
.hero-title{left:110px;top:252px;font-size:36px;line-height:48px;color:var(--white)}
.hero-text{left:112px;top:372px;width:360px;font-size:14px;line-height:28px;color:var(--white)}
.btn{display:flex;align-items:center;justify-content:center;gap:14px;font-family:"Exo 2",sans-serif;font-weight:800;font-size:20px;border-radius:34px}
.btn-ghost-light{left:111px;top:486px;width:220px;height:66px;border:2px solid var(--white);color:var(--white)}
.dots{left:552px;top:641px;display:flex;gap:12px}
.dots span{width:22px;height:22px;border:2px solid var(--white);border-radius:50%}
.dots span:first-child{background:var(--white)}

/* about */
.about-photo{left:0;top:868px;width:566px;height:420px}
.about-title{left:644px;top:866px;font-size:46px}
.about-text{left:645px;top:950px;width:440px;font-size:14px;line-height:20.5px;color:var(--text)}
.btn-outline{border:2px solid var(--red);color:var(--red);background:var(--white);box-shadow:0 8px 18px rgba(0,0,0,.12)}
.about-more{left:645px;top:1189px;width:220px;height:62px}

/* services */
.section-title{font-size:46px;text-align:center}
.rule{height:3px;background:var(--red);width:124px}
.services-title{left:0;top:1418px;width:1200px}
.services-rule{left:538px;top:1493px}
.svc-photo{box-shadow:0 10px 24px rgba(0,0,0,.2)}
.svc-frame{border-left:10px solid var(--black);border-top:10px solid var(--black);border-bottom:10px solid var(--black)}
.svc-card{display:flex;flex-direction:column;align-items:center;text-align:center;color:var(--white);padding-top:34px}
.svc-card h3{font-family:"Exo 2",sans-serif;font-weight:800;font-size:31px;margin-bottom:24px}
.svc-card p{font-size:14px;line-height:20px;width:380px;margin-bottom:18px}
.btn-ghost{width:222px;height:60px;border:2px solid var(--white);color:var(--white);font-size:19px}
.svc-card.red{background:var(--red)}
.svc-card.dark{background:var(--black)}
.section-more{left:492px;top:3126px;width:216px;height:60px;background:var(--red);color:var(--white);font-size:19px;box-shadow:0 8px 18px rgba(0,0,0,.2)}

/* blog */
.blog-title{left:108px;top:3276px;font-size:42px}
.blog-rule{left:110px;top:3340px;width:150px}
.blog-card{overflow:hidden}
.blog-card .caption{position:absolute;left:44px;bottom:56px;font-family:"Exo 2",sans-serif;font-weight:800;color:var(--white);text-transform:uppercase;letter-spacing:1px}
.blog-card.big .caption{font-size:23px;line-height:31px}
.blog-card.small .caption{left:30px;bottom:38px;font-size:16px;line-height:24px}

/* form */
.contact-title{left:0;top:3898px;width:1200px}
.contact-rule{left:524px;top:3988px;width:152px}
.field{border:2px solid var(--field);font-family:"Exo 2",sans-serif;font-weight:700;font-size:19px;color:var(--field);padding:34px 0 0 27px}
.field.msg{padding-top:32px}
.submit{left:457px;top:4482px;width:220px;height:60px;border:2px solid var(--red);color:var(--red);font-size:26px;box-shadow:0 8px 16px rgba(0,0,0,.12)}

/* footer */
.footer{left:0;top:4600px;width:1200px;height:425px}
.foot-brand{left:114px;top:4725px;text-align:center;color:var(--white)}
.foot-brand .brand-dot{margin:0 auto 10px}
.foot-brand .brand-name{color:var(--white);font-size:38px}
.social{left:136px;top:4848px;display:flex;gap:40px}
.social span{width:40px;height:40px;border-radius:50%;background:var(--white)}
.foot-head{font-family:"Exo 2",sans-serif;font-weight:700;font-size:22px;color:var(--white);letter-spacing:1px}
.foot-links{left:561px;top:4772px;font-size:14px;line-height:26px;color:var(--white);text-transform:uppercase;list-style:none}
.foot-contact{left:845px;top:4753px;color:var(--white);font-size:14px}
.foot-contact .row{display:flex;align-items:flex-start;gap:22px;margin-bottom:20px}
.foot-contact svg{flex:none}
.copyright{left:0;top:4967px;width:1200px;height:58px;background:var(--red);color:var(--white);font-size:14px;text-align:center;line-height:58px}
</style>
</head>
<body>
<div class="page">

  <!-- header -->
  <header class="topbar abs">
    <svg class="contact-strip abs" width="697" height="68" viewBox="0 0 697 68"><polygon points="20,0 697,0 697,68 0,68" fill="#d0202c"/></svg>
    <div class="abs" style="left:503px;top:0;width:697px;height:68px">
      <div class="item" style="left:70px;position:absolute;top:20px;color:#fff;font-size:15px;display:flex;align-items:center;gap:14px">
        <svg width="34" height="24" viewBox="0 0 34 24"><rect x="1" y="1" width="32" height="22" fill="#fff"/><polyline points="1,1 17,14 33,1" fill="none" stroke="#d0202c" stroke-width="2.5"/></svg>
        TwistyLanesCamp@mailbox.com
      </div>
      <div class="item phone-box" style="position:absolute;left:396px;top:12px;color:#fff;display:flex;align-items:center;gap:14px">
        <svg width="24" height="24" viewBox="0 0 24 24"><circle cx="12" cy="12" r="11" fill="#fff"/><path d="M8 6l2 3-1.5 1.5a9 9 0 0 0 5 5L15 14l3 2-1 2.5C11 18 6 13 5.5 7z" fill="#d0202c"/></svg>
        040-512730
      </div>
    </div>
    <div class="brand abs">
      <span class="brand-dot"></span>
      <span class="brand-name">TwistyLanes<small>Camp.com</small></span>
    </div>
    <nav class="nav abs">
      <span>About ▾</span><span>Trails &amp; Tales</span><span>The Smart Rver</span><span>Women On The road</span><span>Bad RV</span><span>Blog</span><span>Contact</span>
    </nav>
  </header>

  <!-- hero -->
  <section class="hero abs" role="img" aria-label="Motorhome parked on an autumn forest road with golden trees"></section>
  <svg class="abs" style="left:0;top:620px" width="1200" height="110" viewBox="0 0 1200 110"><path d="M0 30 C200 60 330 90 520 100 L0 110Z" fill="#d0202c"/><path d="M0 80 C250 95 400 100 600 104 L600 110 L0 110Z" fill="#e35a62"/><rect x="0" y="100" width="1200" height="10" fill="#fff"/></svg>
  <h1 class="hero-title heading abs">LESSION FORM<br><span class="accent">THE ROAD</span></h1>
  <p class="hero-text abs">If you're anxious for more fun and fewer bumps on the road to adventure , we can help.</p>
  <div class="btn btn-ghost-light abs">GET STARTED
    <svg width="30" height="22" viewBox="0 0 30 22"><path d="M2 11h25M18 2l9 9-9 9" fill="none" stroke="#fff" stroke-width="3"/></svg></div>
  <div class="dots abs"><span></span><span></span><span></span></div>

  <!-- about -->
  <svg class="about-photo abs" width="566" height="420" viewBox="0 0 566 420">
    <polygon points="0,0 70,0 40,420 0,420" fill="#d0202c"/>
    <polygon points="538,0 566,0 512,420 500,420" fill="#d0202c"/>
  </svg>
  <div class="abs" role="img" aria-label="Motorhome parked in a green meadow with trees, with a play button" style="left:40px;top:868px;width:516px;height:420px;background:linear-gradient(160deg,#3f4a3a,#6a7a5a 55%,#4c5a38);clip-path:polygon(30px 0,516px 0,470px 420px,0 420px)"></div>
  <svg class="abs" style="left:238px;top:1036px" width="80" height="80" viewBox="0 0 80 80"><circle cx="40" cy="40" r="36" fill="none" stroke="#fff" stroke-width="4"/><polygon points="32,24 58,40 32,56" fill="#fff"/></svg>
  <h2 class="about-title heading abs">ABOUT <span class="accent">US</span></h2>
  <p class="about-text abs">My wife and I have been RVing since 2007. We have had two Super C's and two Class A motor homes. We are not full timers but we have spent a lot of time on the road.Like many of you, we started cold. No lessons and very little in the way of education from the RV dealers who sold us our coaches. Our first RV initi ation was done in 20 minutes by a drunken employee who barely made it through his all too brief "brief". But there we wereNaively happy. Little did we know that there was much to learn before to we could smoothen the road to adventure.</p>
  <div class="btn btn-outline about-more abs">MORE
    <svg width="34" height="24" viewBox="0 0 34 24"><path d="M2 12h28M20 3l10 9-10 9" fill="none" stroke="#d0202c" stroke-width="3.5"/></svg></div>

  <!-- services -->
  <h2 class="section-title heading services-title abs"><span class="accent">OUR</span> SERVICES</h2>
  <div class="rule services-rule abs" style="width:124px"></div>

  <div class="svc-frame abs" style="left:113px;top:1628px;width:150px;height:326px"></div>
  <div class="svc-photo abs" role="img" aria-label="White motorhome on a desert road with a traveller taking photos" style="left:457px;top:1604px;width:630px;height:376px;background:linear-gradient(110deg,#8c8c8c,#e6e0d6 40%,#b98d6a 70%,#c9ab8c)"></div>
  <div class="svc-card red abs" style="left:123px;top:1638px;width:439px;height:308px">
    <h3>Traile &amp; Tales</h3>
    <p>It was a steady downpour that day in rural Mississipp It was a steady downpour that day in rural</p>
    <div class="btn btn-ghost">MORE <svg width="34" height="22" viewBox="0 0 34 22"><path d="M2 11h28M21 2l9 9-9 9" fill="none" stroke="#fff" stroke-width="2.5"/></svg></div>
  </div>

  <div class="svc-photo abs" role="img" aria-label="Woman and dog resting in the open back of a camper van" style="left:111px;top:2115px;width:630px;height:375px;background:linear-gradient(110deg,#3a4a7a,#d8d8d8 35%,#e5c0a8 60%,#5a6a4a)"></div>
  <div class="abs" style="left:936px;top:2141px;width:148px;height:325px;border-right:8px solid #d0202c;border-top:8px solid #d0202c;border-bottom:8px solid #d0202c"></div>
  <div class="svc-card dark abs" style="left:638px;top:2150px;width:438px;height:308px">
    <h3>The Smart Rver</h3>
    <p>Towables: Should you go cheap and cheerful when We have owned three motorhomes; two class A motorhomes and</p>
    <div class="btn btn-ghost">MORE <svg width="34" height="22" viewBox="0 0 34 22"><path d="M2 11h28M21 2l9 9-9 9" fill="none" stroke="#fff" stroke-width="2.5"/></svg></div>
  </div>

  <div class="svc-frame abs" style="left:113px;top:2658px;width:150px;height:326px"></div>
  <div class="svc-photo abs" role="img" aria-label="Woman with a backpack looking over a mountain road" style="left:457px;top:2634px;width:630px;height:374px;background:linear-gradient(110deg,#6a5a3a,#d9c090 30%,#8a9a88 60%,#b8c0c4)"></div>
  <div class="svc-card red abs" style="left:123px;top:2668px;width:439px;height:308px">
    <h3>Women On The Road</h3>
    <p>When we talk to couples on the road, especially Mot! Whew...just finished another article, need a break Ladies and Gent you</p>
    <div class="btn btn-ghost">MORE <svg width="34" height="22" viewBox="0 0 34 22"><path d="M2 11h28M21 2l9 9-9 9" fill="none" stroke="#fff" stroke-width="2.5"/></svg></div>
  </div>

  <div class="btn section-more abs">MORE <svg width="34" height="24" viewBox="0 0 34 24"><path d="M2 12h28M20 3l10 9-10 9" fill="none" stroke="#fff" stroke-width="3.5"/></svg></div>

  <!-- blog -->
  <h2 class="blog-title heading abs">LETEST <span class="accent">BLOG</span></h2>
  <div class="rule blog-rule abs"></div>
  <div class="blog-card big abs" role="img" aria-label="Family walking beside a travel trailer by a mountain lake" style="left:111px;top:3407px;width:535px;height:448px;background:linear-gradient(160deg,#9a9a9a,#6a6e6a 50%,#3a4a4a)">
    <div class="caption">RV ENVY? WHY YOU WILL<br>ALWAYS WANT A DIFFERENT ONE!</div>
  </div>
  <div class="blog-card small abs" role="img" aria-label="Campers sitting outside a travel trailer" style="left:667px;top:3407px;width:420px;height:202px;background:linear-gradient(160deg,#7a7c7a,#4a4a44 60%,#6a5a3a)">
    <div class="caption">RV ENVY? WHY YOU WILL<br>ALWAYS WANT A DIFFERENT ONE!</div>
  </div>
  <div class="blog-card small abs" role="img" aria-label="Motorhome parked by a river in autumn" style="left:667px;top:3629px;width:420px;height:226px;background:linear-gradient(160deg,#9aa0a4,#6a5a44 55%,#5a4a34)">
    <div class="caption">RV HELL: DRIVING OFF WITHOUT<br>YOUR WIFE!</div>
  </div>

  <!-- contact form -->
  <h2 class="section-title heading contact-title abs">CONTACT <span class="accent">FORM</span></h2>
  <div class="rule contact-rule abs"></div>
  <div class="field abs" style="left:113px;top:4067px;width:468px;height:95px">First Name :</div>
  <div class="field abs" style="left:599px;top:4067px;width:488px;height:95px">Last Name :</div>
  <div class="field abs" style="left:113px;top:4177px;width:468px;height:96px">Email Address :</div>
  <div class="field abs" style="left:599px;top:4177px;width:488px;height:96px">Mobil Number :</div>
  <div class="field msg abs" style="left:113px;top:4288px;width:974px;height:129px">Message :</div>
  <div class="btn submit abs">SUBMIT</div>

  <!-- footer -->
  <svg class="footer abs" width="1200" height="425" viewBox="0 0 1200 425">
    <rect x="0" y="20" width="1200" height="405" fill="#0c0c0c"/>
    <path d="M0 20 L0 0 L1200 0 L1200 30 C900 30 700 40 0 20Z" fill="#fff"/>
    <path d="M640 20 C850 30 1050 50 1200 80 L1200 30 C1050 30 850 24 640 20Z" fill="#d0202c"/>
    <path d="M760 26 C950 40 1100 60 1200 95 L1200 80 C1050 50 900 34 760 26Z" fill="#e35a62"/>
  </svg>
  <div class="foot-brand abs">
    <span class="brand-dot" style="display:block"></span>
    <span class="brand-name">TwistyLanes<small>Camp.com</small></span>
  </div>
  <div class="social abs"><span></span><span></span><span></span></div>
  <div class="foot-head abs" style="left:559px;top:4720px">QUICK LINKS</div>
  <ul class="foot-links abs">
    <li>About us</li><li>Trails &amp; Tales</li><li>The Smart Rver</li><li>Women on the Road</li><li>Bad RV</li>
  </ul>
  <div class="foot-head abs" style="left:844px;top:4720px">CONTECT US</div>
  <div class="foot-contact abs" style="top:4768px">
    <div class="row"><svg width="22" height="22" viewBox="0 0 24 24"><circle cx="12" cy="12" r="11" fill="#fff"/><path d="M8 6l2 3-1.5 1.5a9 9 0 0 0 5 5L15 14l3 2-1 2.5C11 18 6 13 5.5 7z" fill="#0c0c0c"/></svg><span>040-512730</span></div>
    <div class="row"><svg width="22" height="16" viewBox="0 0 34 24"><rect x="1" y="1" width="32" height="22" fill="#fff"/><polyline points="1,1 17,14 33,1" fill="none" stroke="#0c0c0c" stroke-width="2.5"/></svg><span>TwistyLanesCamp@mailbox.com</span></div>
    <div class="row"><svg width="22" height="26" viewBox="0 0 22 26"><path d="M11 1a9 9 0 0 0-9 9c0 7 9 15 9 15s9-8 9-15a9 9 0 0 0-9-9z" fill="#fff"/><circle cx="11" cy="10" r="3.5" fill="#0c0c0c"/></svg><span>Pine Street &nbsp;Ashford<br>NC 27014</span></div>
  </div>
  <div class="copyright abs">Copyright © 2021 Twisty Lanes Camp. All rights reserved. Coded by Ridgeway Studio</div>

</div>
</body>
</html>
```